Business Card for Pet Food Deliver

Looking for a business card design for a start up company. We are Brisk Hound, Premium Pet Products Brought Round.

We market and are designing a website where our clients can go to and order pet food. We then deliver to a local client base. We do person to person deliver, we do not ship at this point. We are starting off with dog and cat food and treats.

Attached is our logo. We are looking for a fun yet professional design. Eye catching with color but not over the top with color. Looking for a double sided card. Contact info on the front and our logo on the back maybe. . .

I am a huge green fan. However, I am thinking I like the orange a bit more then the blue and green for dominant colors. . .

I am attaching our logo.

The file that has our slogan under has a minor change not implemented yet. The word 'Premium' should be gray to match and the word 'Delivered' should be black to match.

Target Market(s)

We are looking to service those pet owners looking for the convenience of not having to drive to a pet store to purchase their products. We are looking for those who are web savvy and purchase online.

We will also be targeting seniors in senior communities without consistent transprotation.

Industry/Entity Type

Pet

Font styles to use
Sans Serif

Colors
f37122
3176b5
acd036

Requirements
Must have
• Double sided. Logo only on one side with a bold color for the background.

Space for name, phone number, website address, mailing address.
Should not have
• No paws, delivery trucks.

```html
<!DOCTYPE html>
<html lang="en">
<head>
<meta charset="utf-8">
<title>Brisk Hound – Business Card</title>
<link href="https://fonts.googleapis.com/css2?family=Open+Sans:wght@400;700&display=swap" rel="stylesheet">
<style>
  :root {
    --orange: #f37122;
    --green: #acd036;
    --blue: #3176b5;
    --sky: #2e9fd6;
    --paper: #f4f4f2;
    --ink-grey: #5b5b5d;
    --ink-dark: #58585a;
    --tagline-grey: #9a9a9c;
    --tagline-black: #1e1e1e;
    --backdrop: #e8e6e3;
    --illustration-tint: #e5661c;
  }
  * { box-sizing: border-box; margin: 0; padding: 0; }
  html, body {
    width: 1200px; height: 997px; overflow: hidden;
    background: var(--backdrop);
    font-family: "Open Sans", Verdana, sans-serif;
  }
  .sheet {
    width: 1200px; height: 997px;
    display: flex; flex-direction: column;
    align-items: center; justify-content: center; gap: 60px;
  }
  .card {
    position: relative;
    width: 700px; height: 400px;
    overflow: hidden;
    box-shadow: 0 6px 18px rgba(0,0,0,0.12);
  }

  /* Logo side */
  .card--logo { background: var(--paper); display: flex; }
  .stripes { display: flex; height: 100%; }
  .stripe { width: 105px; height: 100%; }
  .stripe--orange { background: var(--orange); }
  .stripe--green { background: var(--green); }
  .stripe--blue { background: var(--sky); }
  .brand {
    flex: 1;
    display: flex; flex-direction: column;
    align-items: center; justify-content: center;
    padding-top: 40px;
  }
  .brand__mark {
    display: flex; align-items: center; gap: 12px;
  }
  .brand__dot {
    width: 18px; height: 18px; border-radius: 50%;
    background: var(--orange);
  }
  .brand__name {
    font-size: 50px; font-weight: 400;
    color: var(--ink-grey);
    letter-spacing: -0.5px;
    line-height: 1;
  }
  .brand__tagline {
    margin-top: 12px;
    font-size: 11.5px; letter-spacing: 0.6px;
    text-transform: uppercase;
    color: var(--tagline-grey);
  }
  .brand__tagline strong { color: var(--tagline-black); font-weight: 400; }

  /* Contact side */
  .card--contact { background: var(--orange); }
  .illustration {
    position: absolute; left: 40px; bottom: 0;
    width: 300px; height: 290px;
    background: linear-gradient(160deg, var(--illustration-tint), var(--orange) 85%);
    border-radius: 0 80px 0 0;
  }
  .contact {
    position: absolute; right: 40px; top: 42px;
    text-align: right; color: #fff;
  }
  .contact__name { font-size: 19px; font-weight: 700; line-height: 1.25; }
  .contact__role { font-size: 19px; font-weight: 700; color: var(--ink-dark); line-height: 1.25; }
  .contact__details {
    margin-top: 34px;
    font-size: 17px; line-height: 1.4; font-style: normal;
  }
  .contact__web { font-weight: 700; }
  .contact__address { margin-top: 6px; }
</style>
</head>
<body>
<main class="sheet">
  <section class="card card--logo" aria-label="Business card, logo side">
    <div class="stripes">
      <div class="stripe stripe--orange"></div>
      <div class="stripe stripe--green"></div>
      <div class="stripe stripe--blue"></div>
    </div>
    <div class="brand">
      <div class="brand__mark">
        <span class="brand__dot"></span>
        <span class="brand__name">Brisk Hound</span>
      </div>
      <p class="brand__tagline">Premium pet products <strong>brought round</strong></p>
    </div>
  </section>

  <section class="card card--contact" aria-label="Business card, contact side">
    <div class="illustration" role="img" aria-label="Large line drawing of the brand mascot in dark grey on orange"></div>
    <div class="contact">
      <p class="contact__name">Daniel Whitford</p>
      <p class="contact__role">Nutrition Specialist</p>
      <address class="contact__details">
        <div>555-014-2280</div>
        <div>daniel@BriskHoundRounds.com</div>
        <div class="contact__web">www.BriskHoundRounds.com</div>
        <div class="contact__address">4820 Larchmont Lane</div>
        <div>Alder Falls, WI 54000</div>
      </address>
    </div>
  </section>
</main>
</body>
</html>
```